Vexa Grease street sign

looking for a fresh new looking street sign .. sized 6ft tall 5ft wide <br/>"Vexa Grease<br/>The Precision Crew"<br/>remove "... and Tune"<br/>remove "Quarn" the bottom should just read "The Precision Crew"

Target Market(s)

motorist passing my location

Industry/Entity Type

Automotive

Font styles to use
Sans Serif

Requirements
Must have
• Vexa Grease
• The Precision Crew
Should not have
• NO reference to "Quarn"

```html
<!DOCTYPE html>
<html lang="en">
<head>
<meta charset="UTF-8">
<title>Vexa Grease – Street Sign</title>
<link href="https://fonts.googleapis.com/css2?family=Roboto:wght@700&display=swap" rel="stylesheet">
<style>
  :root {
    --brand-navy: #0a0e4a;
    --band-red: #e01f2a;
    --navy-top: #0a0e36;
    --navy-bottom: #08104f;
    --navy-edge: #23237a;
    --sign-white: #ffffff;
    --flag-tone-dark: #1a1a1a;
    --flag-tone-light: #d9d9d9;
  }
  html, body {
    margin: 0;
    padding: 0;
    width: 900px;
    height: 1200px;
    overflow: hidden;
    background: var(--sign-white);
  }
  .sign {
    position: relative;
    width: 900px;
    height: 1200px;
    overflow: hidden;
  }
  .sign-backdrop {
    position: absolute;
    inset: 0;
  }
  .brand-name {
    position: absolute;
    top: 170px;
    left: 0;
    width: 100%;
    margin: 0;
    text-align: center;
    font-family: "Roboto", Arial, sans-serif;
    font-weight: 700;
    font-size: 124px;
    line-height: 140px;
    color: var(--brand-navy);
  }
  .tagline {
    position: absolute;
    top: 890px;
    left: 0;
    width: 100%;
    margin: 0;
    text-align: center;
    font-family: "Roboto", Arial, sans-serif;
    font-weight: 700;
    font-size: 92px;
    line-height: 112px;
    color: var(--sign-white);
  }
  .tagline span { display: block; }
</style>
</head>
<body>
  <main class="sign">
    <svg class="sign-backdrop" width="900" height="1200" viewBox="0 0 900 1200" xmlns="http://www.w3.org/2000/svg">
      <defs>
        <linearGradient id="navyFill" x1="0" y1="0" x2="0" y2="1">
          <stop offset="0" stop-color="var(--navy-top)"/>
          <stop offset="1" stop-color="var(--navy-bottom)"/>
        </linearGradient>
        <linearGradient id="flagTone" x1="0" y1="0" x2="1" y2="1">
          <stop offset="0" stop-color="var(--flag-tone-dark)"/>
          <stop offset="0.5" stop-color="var(--flag-tone-light)"/>
          <stop offset="1" stop-color="var(--flag-tone-dark)"/>
        </linearGradient>
      </defs>
      <rect class="navy-field" width="900" height="1200" fill="url(#navyFill)"/>
      <path class="navy-edge" d="M0 470 Q450 760 900 470 V520 Q450 790 0 520 Z" fill="var(--navy-edge)"/>
      <path class="red-sweep" d="M0 440 Q450 760 900 440 V478 Q450 790 0 478 Z" fill="var(--band-red)"/>
      <path class="white-field" d="M0 0 H900 V440 Q450 725 0 440 Z" fill="var(--sign-white)"/>
      <rect class="crossed-flags" x="230" y="520" width="440" height="310" rx="24"
            fill="url(#flagTone)" role="img" aria-label="Two crossed black-and-white checkered racing flags"/>
    </svg>

    <h1 class="brand-name">Vexa Grease</h1>
    <p class="tagline"><span>The</span><span>Precision Crew</span></p>
  </main>
</body>
</html>
```